Velvet Paws Website - Boutique online pet store for both owners, their homes and their dogs

I need a high end online store for the sale of dog products (collars, leashes, coats etc), products for their owners (pyjamas, cosmetic bags, pencil cases, gift wrapping paper, greeting cards etc) and the owners home (ring holders, cushion covers, throws etc).

Please peruse the following website for a vauge idea of slightly similar stores:

Mybeaglecorner.com.au
Pebblepuphaven.com.au
Terrierplace.com.au
Tallhound.co.za

Please keep in mind these are breed specific sites. I intend for the business to sell to trending dog breeds, for example, currently in Australia, French Bulldogs and Dachshunds are trending; therefore this will be the business's current focus.

I also intend for this website to be more elegant and refined than the websites mentioned above. Similar to top names brands, with a hint of cuteness to appeal to the animal lover within customers.

Target Market(s)

Velvet Paws' target market is majority females, late 20's - 40's, either single, in a relationship, or with children who have left the home. They own small and pampered dogs and treat these dogs like their children. They will have a high disposable income.

I want the brand to attract elitist clientele. Comment has been made that people mightn't be able to spell Velvet when searching for the website; those are not the type of customers I want to attract. I think it may be difficult to encapsulate these two target ideas into the brand; I'd like is to appeal to both the 'Melbourne Socialite' and the Noosa stereotype of "I'm too cool to show it, but I really care what you think"

The products will be, for the most part, unique to the market, a few examples include:

custom hand made collars and leads reflecting current human fashion trends;
leather coats for dogs;
flannel pyjamas for dog;
chef's hats for dogs;
furniture which incorporates dogs beds (blanket box, coffee table, bedside table)
bags, cushions, throw rugs, pyjamas made from various dog print fabrics;
fine leather handbags and purses with various and discreet dog themed embellishments;
custom gift wrapping paper etc etc

Amazing customer service and high quality are two of the core values of Velvet Paws.

The business will be run through the website as well as high-end markets around Brisbane, Gold Coast and Sunshine Coast.

Colors
eea4c8
ffffff
e34197

Requirements
Must have
• MUST BE FULLY OPERATIONAL ON COMPLETION. I own the domain name www.velvetpaws-example.com.au. Needs to be functioning on this domain with an operational online store using Payvora.
• Must also be mobile friendly.
• Pages:
• For your pup (shopping page)
• For your home (shopping page)
• For you (shopping page)
• Stationery
• Contact us
• I am open to better and more creative page names.
• MUST have an easy to operate back end that I can use to update products as and when required.

```html
<!DOCTYPE html>
<html lang="en">
<head>
<meta charset="utf-8">
<title>Velvet Paws – Boutique for Dogs and Their People</title>
<link rel="stylesheet" href="https://fonts.googleapis.com/css2?family=Source+Sans+3:wght@400;600;700&family=Roboto+Condensed:wght@400;500&display=swap">
<style>
:root{
  --pink:#f06aa6;
  --pink-soft:#eea4c8;
  --pink-deep:#e34197;
  --ink:#2b2f33;
  --slate:#3b4144;
  --navy:#1c2e4a;
  --grey:#7a7f83;
  --line:#e3e5e6;
  --mist:#c9d3d6;
  --btn-grey:#d5d8d9;
  --white:#ffffff;
}
*{box-sizing:border-box;margin:0;padding:0}
html,body{width:675px;height:1200px;overflow:hidden;background:var(--white)}
body{position:relative;font-family:"Source Sans 3",sans-serif;color:var(--ink);font-size:7.5px}
.abs{position:absolute}
a{color:inherit;text-decoration:none}

/* top bar */
.topbar{left:0;top:0;width:675px;height:27px;border-bottom:1px solid var(--line);font-size:7px;text-transform:uppercase}
.topbar .left{left:29px;top:9px}
.topbar .right{right:29px;top:9px;display:flex;align-items:center;gap:4px}
.sep{margin:0 7px;color:var(--grey)}
.logo{left:0;top:30px;width:675px;text-align:center}
.logo-mark{display:inline-block;width:18px;height:18px;background:var(--pink);margin-bottom:3px}
.logo-name{font-weight:700;font-size:14px;color:var(--navy);letter-spacing:.5px;text-transform:uppercase}

/* nav */
.nav{left:0;top:82px;width:675px;height:26px;background:var(--pink)}
.nav ul{list-style:none;display:flex;position:absolute;left:29px;top:0;height:26px}
.nav li{color:var(--white);font-size:7px;font-weight:600;text-transform:uppercase;line-height:26px;padding:0 12px}
.nav li.active{background:var(--pink-deep)}
.search{right:29px;top:6px;width:96px;height:15px;background:var(--white);font-size:6px;color:#aaa;font-style:italic;padding:3px 5px}
.search svg{position:absolute;right:4px;top:3px}

/* hero */
.hero{left:0;top:108px;width:675px;height:226px;background:linear-gradient(180deg,#4fa6d3 0%,#7bb4d0 45%,#c9c2bb 62%,#bdb4ab 100%)}
.hero-photo{left:40px;top:75px;width:260px;height:115px;background:linear-gradient(135deg,#d9b0c6,#9db08a);border-radius:40px;opacity:.85}
.hero-copy{left:304px;top:50px;width:340px;text-align:center;color:var(--white);font-family:"Roboto Condensed",sans-serif;white-space:nowrap}
.hero-copy .k1{font-size:23px;line-height:1}
.hero-copy .k2{font-size:31px;line-height:1.15;letter-spacing:-.3px}
.hero-copy .k3{font-size:10px;margin-top:6px;display:flex;align-items:center;justify-content:center;gap:6px}
.hero-copy .k3 i{display:block;width:36px;height:1px;background:var(--white)}
.btn-pink{background:var(--pink);color:var(--white);font-weight:600;text-transform:uppercase;display:inline-block;text-align:center}
.hero-btn{left:425px;top:255px;width:99px;height:22px;line-height:22px;font-size:10px}

/* categories */
.cat{top:347px;width:197px;height:104px;color:var(--white)}
.cat .t{position:absolute;left:18px;top:22px;font-family:"Roboto Condensed",sans-serif;font-size:16px;text-transform:uppercase}
.cat .s{position:absolute;left:18px;top:44px;font-size:7px;text-transform:uppercase}
.cat .b{position:absolute;left:18px;top:59px;width:65px;height:17px;line-height:17px;font-size:7px}

/* section titles */
.sec-title{font-size:12.5px;color:var(--pink);text-transform:uppercase;font-weight:400}
.rule{height:1px;background:var(--line)}
.arrows{display:flex;gap:2px}
.arrows span{display:block;background:var(--btn-grey);position:relative}

/* products */
.prod{top:502px;width:113px}
.prod .img{height:104px;border:1px solid var(--line);position:relative}
.prod .img div{position:absolute;left:20px;top:14px;right:20px;bottom:14px;border-radius:6px}
.prod .name{font-size:7px;text-align:center;margin-top:8px;line-height:1.6}
.prod .price{font-size:10px;font-weight:600;text-align:center;margin-top:5px}
.prod .act{display:flex;justify-content:center;gap:2px;margin-top:7px}
.prod .cart{width:65px;height:17px;line-height:17px;font-size:7px;font-weight:600;color:var(--white);background:var(--slate);text-align:center;text-transform:uppercase}
.prod .cart.pink{background:var(--pink)}
.prod .wish{width:17px;height:17px;background:var(--btn-grey);display:flex;align-items:center;justify-content:center}

/* news / about / popular */
.news-img{left:29px;top:742px;width:197px;height:104px;background:linear-gradient(135deg,#a9cbe0,#e7d6c5 60%,#c7a98d)}
.news-h{left:29px;top:853px;font-size:9px;font-weight:600}
.news-date{left:29px;top:873px;font-size:6.5px;color:var(--grey)}
.news-p{left:29px;top:885px;width:200px;font-size:6.8px;line-height:1.65;color:#555}
.about{left:239px;top:742px;width:197px;height:191px;background:var(--slate);color:#e7e9ea;padding:14px 16px;font-size:6.8px;line-height:1.7;text-align:justify}
.about p+p{margin-top:6px}
.about .btn-pink{margin-top:10px;width:65px;height:19px;line-height:19px;font-size:7px}
.pop{left:449px;width:197px;height:62px}
.pop .thumb{position:absolute;left:0;top:0;width:70px;height:60px;border:1px solid var(--line)}
.pop .thumb div{position:absolute;left:12px;top:10px;right:12px;bottom:10px;border-radius:4px}
.pop .n{position:absolute;left:80px;top:0;width:115px;font-size:7.2px;line-height:1.7}
.pop .o{position:absolute;left:80px;top:34px;font-size:6.5px;color:#999;text-decoration:line-through}
.pop .p{position:absolute;left:80px;top:44px;font-size:10px;font-weight:600}

/* newsletter */
.newsletter{left:0;top:966px;width:675px;height:46px;background:var(--mist)}
.env{left:80px;top:-10px;width:52px;height:44px;background:linear-gradient(135deg,#9cd35a,#f4c13a);transform:rotate(-12deg)}
.nl-t{left:145px;top:11px;font-size:10px;font-weight:700;text-transform:uppercase}
.nl-s{left:145px;top:26px;font-size:7.5px;color:#444}
.nl-form{left:362px;top:11px;width:240px;height:22px;background:var(--white);border:2px solid var(--white)}
.nl-form .ph{position:absolute;left:8px;top:4px;font-size:7.5px;color:#888}
.nl-form .btn-pink{position:absolute;right:0;top:0;width:72px;height:18px;line-height:18px;font-size:7px}

/* footer */
.fcol{top:1042px}
.fcol h4{font-size:10.5px;font-weight:400;color:var(--pink);text-transform:uppercase;margin-bottom:8px}
.fcol li{list-style:none;font-size:7px;line-height:16.3px;color:#333}
.fcontact p{font-size:7px;line-height:13px;color:#333}
.flogo{left:540px;top:1058px;width:110px;text-align:center}
.flogo .logo-mark{width:22px;height:22px}
.bottom-rule{left:0;top:1162px;width:675px;height:1px;background:var(--line)}
.cards{left:29px;top:1175px;display:flex;gap:14px;font-size:7.5px;font-weight:700;color:#b8bcbf;text-transform:uppercase}
.copy{left:0;top:1175px;width:675px;text-align:center;font-size:7px;color:#444}
.social{right:29px;top:1172px;display:flex;align-items:center;gap:4px;font-size:7px}
.social i{display:block;width:13px;height:13px;border-radius:50%}
</style>
</head>
<body>

<header>
  <div class="abs topbar">
    <div class="abs left">My Account<span class="sep">|</span>Wish List (0)<span class="sep">|</span>Checkout</div>
    <div class="abs right">Login<span class="sep">|</span>Register<span class="sep">|</span>
      <svg width="13" height="11" viewBox="0 0 13 11"><path d="M0 1h2.5l2 6.5h6l1.5-4.5H4" fill="none" stroke="#f06aa6" stroke-width="1"/><circle cx="5.5" cy="9.5" r="1" fill="#f06aa6"/><circle cx="9.5" cy="9.5" r="1" fill="#f06aa6"/></svg>
      <span>0 item(s) - $0.00</span></div>
  </div>
  <div class="abs logo">
    <span class="logo-mark"></span><br>
    <span class="logo-name">Velvet Paws</span>
  </div>
  <nav class="abs nav">
    <ul>
      <li class="active">Home</li><li>For Your Pup</li><li>For Your Home</li><li>For You</li><li>Stationery</li><li>About Us</li><li>Contact Us</li>
    </ul>
    <div class="abs search">Search
      <svg width="8" height="8" viewBox="0 0 8 8"><circle cx="3.2" cy="3.2" r="2.3" fill="none" stroke="#f06aa6" stroke-width="1.2"/><path d="M5 5l2.5 2.5" stroke="#f06aa6" stroke-width="1.3"/></svg>
    </div>
  </nav>
</header>

<section class="abs hero">
  <div class="abs hero-photo" role="img" aria-label="Stack of floral handmade dog collars with metal buckles on a wooden deck"></div>
  <div class="abs hero-copy">
    <div class="k1">CUSTOM</div>
    <div class="k2">HANDMADE COLLARS</div>
    <div class="k3"><i></i>CURRENT HUMAN FASHION TRENDS<i></i></div>
  </div>
</section>
<a class="abs btn-pink hero-btn">Shop Now!</a>

<section>
  <div class="abs cat" style="left:29px;background:linear-gradient(90deg,#3e4548,#8a7a68)" role="img" aria-label="Dog wearing a dark leather coat">
    <div class="t">Leather Coats</div><div class="s">For Dogs</div><div class="b btn-pink">Shop Now!</div></div>
  <div class="abs cat" style="left:239px;background:linear-gradient(90deg,#454c55,#b49b6e)" role="img" aria-label="Puppy in flannel pyjamas on a bed">
    <div class="t">Flannel Pyjamas</div><div class="s">For Dogs</div><div class="b btn-pink">Shop Now!</div></div>
  <div class="abs cat" style="left:449px;background:linear-gradient(90deg,#6e4c36,#d9cdc0)" role="img" aria-label="Small white dog in a chef's hat in a kitchen">
    <div class="t">Chef's Hats</div><div class="s">For Dogs</div><div class="b btn-pink">Shop Now!</div></div>
</section>

<section>
  <h2 class="abs sec-title" style="left:29px;top:470px">Featured Products</h2>
  <div class="abs rule" style="left:156px;top:478px;width:434px"></div>
  <div class="abs arrows" style="left:601px;top:466px">
    <span style="width:21px;height:21px"><svg class="abs" style="left:8px;top:7px" width="5" height="7"><path d="M4 0.5L1 3.5L4 6.5" fill="none" stroke="#fff" stroke-width="1.2"/></svg></span>
    <span style="width:21px;height:21px"><svg class="abs" style="left:8px;top:7px" width="5" height="7"><path d="M1 0.5L4 3.5L1 6.5" fill="none" stroke="#fff" stroke-width="1.2"/></svg></span>
  </div>

  <div class="abs prod" style="left:29px">
    <div class="img"><div role="img" aria-label="Small dog in pink pyjamas" style="background:linear-gradient(#f2d2dc,#e7a9c0)"></div></div>
    <p class="name">Simply dummy text of printing<br>typesetting industry.</p><p class="price">$10.00</p>
    <div class="act"><span class="cart pink">Add to Cart</span><span class="wish"><svg width="8" height="7" viewBox="0 0 8 7"><path d="M4 6.5L1 3.5A1.6 1.6 0 0 1 4 1.3A1.6 1.6 0 0 1 7 3.5Z" fill="none" stroke="#888" stroke-width=".8"/></svg></span></div>
  </div>
  <div class="abs prod" style="left:154px">
    <div class="img"><div role="img" aria-label="Small dog in a padded winter coat" style="background:linear-gradient(#d9d6d2,#5b5d60)"></div></div>
    <p class="name">Simply dummy text of printing<br>typesetting industry.</p><p class="price">$10.00</p>
    <div class="act"><span class="cart">Add to Cart</span><span class="wish"><svg width="8" height="7" viewBox="0 0 8 7"><path d="M4 6.5L1 3.5A1.6 1.6 0 0 1 4 1.3A1.6 1.6 0 0 1 7 3.5Z" fill="none" stroke="#888" stroke-width=".8"/></svg></span></div>
  </div>
  <div class="abs prod" style="left:281px">
    <div class="img"><div role="img" aria-label="Colourful leather dog collars" style="background:linear-gradient(135deg,#e9b33c,#2a9a9a 50%,#d94f86)"></div></div>
    <p class="name">Simply dummy text of printing<br>typesetting industry.</p><p class="price">$10.00</p>
    <div class="act"><span class="cart">Add to Cart</span><span class="wish"><svg width="8" height="7" viewBox="0 0 8 7"><path d="M4 6.5L1 3.5A1.6 1.6 0 0 1 4 1.3A1.6 1.6 0 0 1 7 3.5Z" fill="none" stroke="#888" stroke-width=".8"/></svg></span></div>
  </div>
  <div class="abs prod" style="left:407px">
    <div class="img"><div role="img" aria-label="Cream cushion with orange dog print" style="background:linear-gradient(#f5efe6,#f0b48a)"></div></div>
    <p class="name">Simply dummy text of printing<br>typesetting industry.</p><p class="price">$10.00</p>
    <div class="act"><span class="cart">Add to Cart</span><span class="wish"><svg width="8" height="7" viewBox="0 0 8 7"><path d="M4 6.5L1 3.5A1.6 1.6 0 0 1 4 1.3A1.6 1.6 0 0 1 7 3.5Z" fill="none" stroke="#888" stroke-width=".8"/></svg></span></div>
  </div>
  <div class="abs prod" style="left:533px">
    <div class="img"><div role="img" aria-label="Patterned bow tie dog collar" style="background:linear-gradient(#f3d7d9,#c9dcb8)"></div></div>
    <p class="name">Simply dummy text of printing<br>typesetting industry.</p><p class="price">$10.00</p>
    <div class="act"><span class="cart">Add to Cart</span><span class="wish"><svg width="8" height="7" viewBox="0 0 8 7"><path d="M4 6.5L1 3.5A1.6 1.6 0 0 1 4 1.3A1.6 1.6 0 0 1 7 3.5Z" fill="none" stroke="#888" stroke-width=".8"/></svg></span></div>
  </div>
</section>

<div class="abs rule" style="left:29px;top:702px;width:617px;height:2px"></div>

<section>
  <h2 class="abs sec-title" style="left:29px;top:718px">Latest News</h2>
  <div class="abs arrows" style="left:192px;top:718px">
    <span style="width:16px;height:16px"><svg class="abs" style="left:5px;top:6px" width="7" height="5"><path d="M0.5 1L3.5 4L6.5 1" fill="none" stroke="#fff" stroke-width="1.1"/></svg></span>
    <span style="width:16px;height:16px"><svg class="abs" style="left:5px;top:6px" width="7" height="5"><path d="M0.5 4L3.5 1L6.5 4" fill="none" stroke="#fff" stroke-width="1.1"/></svg></span>
  </div>
  <div class="abs news-img" role="img" aria-label="Bulldog in a party hat with 2016 New Year confetti"></div>
  <h3 class="abs news-h">Keeping your dachshund calm on New Years Eve</h3>
  <p class="abs news-date">2015-12-30</p>
  <p class="abs news-p">There are many variations of passages of Lorem Ipsum available, but the majority have suffered alteration in some form, by injected humour look even slightly believable.</p>

  <h2 class="abs sec-title" style="left:239px;top:718px">About Us</h2>
  <div class="abs about">
    <p>It is a long established fact that a reader will be distracted by the readable content of a page when looking at its layout. The point of using Lorem Ipsum is that it has a more-or-less normal distribution of letters, as opposed to using 'Content here, content here', making it look like readable English.</p>
    <p>Many desktop publishing packages and web page editors now use Lorem Ipsum as their default model text, and a search for 'lorem ipsum' will uncover many web sites still in their infancy.</p>
    <span class="btn-pink">Read More</span>
  </div>

  <h2 class="abs sec-title" style="left:449px;top:718px">Popular Products</h2>
  <div class="abs arrows" style="left:612px;top:718px">
    <span style="width:16px;height:16px"><svg class="abs" style="left:5px;top:6px" width="7" height="5"><path d="M0.5 1L3.5 4L6.5 1" fill="none" stroke="#fff" stroke-width="1.1"/></svg></span>
    <span style="width:16px;height:16px"><svg class="abs" style="left:5px;top:6px" width="7" height="5"><path d="M0.5 4L3.5 1L6.5 4" fill="none" stroke="#fff" stroke-width="1.1"/></svg></span>
  </div>
  <div class="abs pop" style="top:742px">
    <div class="thumb"><div role="img" aria-label="Cushion with grey terrier print" style="background:linear-gradient(#f1ece4,#b7b3ae)"></div></div>
    <p class="n">Simply dummy text of printing typesetting industry.</p><p class="o">$15.00</p><p class="p">$10.00</p>
  </div>
  <div class="abs pop" style="top:808px">
    <div class="thumb"><div role="img" aria-label="Checked bow tie collar" style="background:linear-gradient(#e5c9cf,#aab2b8)"></div></div>
    <p class="n">Simply dummy text of printing typesetting industry.</p><p class="o">$15.00</p><p class="p">$10.00</p>
  </div>
  <div class="abs pop" style="top:874px">
    <div class="thumb"><div role="img" aria-label="Red patterned dog pyjamas" style="background:linear-gradient(#e5434f,#c8202e)"></div></div>
    <p class="n">Simply dummy text of printing typesetting industry.</p><p class="o">$15.00</p><p class="p">$10.00</p>
  </div>
</section>

<section class="abs newsletter">
  <div class="abs env" role="img" aria-label="Yellow and green envelopes"></div>
  <h3 class="abs nl-t">Subscribe Our Newsletter</h3>
  <p class="abs nl-s">Don't miss invaluable offer, important update &amp; more!</p>
  <div class="abs nl-form"><span class="ph">E-mail Address</span><span class="btn-pink">Subscribe</span></div>
</section>

<footer>
  <div class="abs fcol" style="left:29px"><h4>Information</h4><ul><li>- About Us</li><li>- Contact us</li><li>- Store Locations</li><li>- Site Map</li><li>- Customer Testimonials</li></ul></div>
  <div class="abs fcol" style="left:138px"><h4>Service</h4><ul><li>- Contact Us</li><li>- Privacy Policy</li><li>- Terms And Conditions</li></ul></div>
  <div class="abs fcol" style="left:240px"><h4>Shopping</h4><ul><li>- For your pup</li><li>- For your home</li><li>- For you</li><li>- Stationery</li></ul></div>
  <div class="abs fcol" style="left:330px"><h4>Help</h4><ul><li>- FAQs</li><li>- Feedback</li><li>- Complain</li></ul></div>
  <div class="abs fcol fcontact" style="left:405px"><h4>Contact Us</h4>
    <p>Lorem Ipsum is simply dummy<br>Maplewood, QL 4T2 9K1</p>
    <p style="margin-top:6px">Phone : +61 7 5550 1234</p>
    <p style="margin-top:3px">Email: hello@velvetpaws-example.com</p>
  </div>
  <div class="abs flogo"><span class="logo-mark"></span><br><span class="logo-name">Velvet Paws</span></div>

  <div class="abs bottom-rule"></div>
  <div class="abs cards"><span>Cardia</span><span>PayLink</span><span>Novex</span></div>
  <p class="abs copy">Copyright © 2016 Velvet Paws, All Rights Reserved</p>
  <div class="abs social">Follow Us:
    <i style="background:#3b5b98"></i><i style="background:#2fa8e0"></i><i style="background:#1a7bb8"></i><i style="background:#e0483a"></i>
  </div>
</footer>

</body>
</html>
```